KORBALT

The business want a professional looking business card. We have a scetch we will add but want the extra upgrade, and would like more suggestions for variations of our business cards.

```html
<!DOCTYPE html>
<html lang="en">
<head>
<meta charset="utf-8">
<title>KORBALT – Business Card</title>
<link rel="stylesheet" href="https://fonts.googleapis.com/css2?family=Cinzel:wght@500;600&family=Montserrat:wght@400;500&display=swap">
<style>
  :root {
    --backdrop: #d9d5ce;
    --card-light: #f6efdd;
    --card-mid: #ede3c8;
    --ink-brown: #5a3d1c;
    --gold: #9a7632;
    --icon: #6b5a44;
    --shadow: rgba(60, 50, 35, 0.28);
  }
  * { margin: 0; padding: 0; box-sizing: border-box; }
  html, body {
    width: 1200px; height: 805px; overflow: hidden;
    background: var(--backdrop);
  }
  .canvas { position: relative; width: 1200px; height: 805px; }
  .card {
    position: absolute; top: 229px; width: 502px; height: 346px;
    background: linear-gradient(135deg, var(--card-mid) 0%, var(--card-light) 55%, var(--card-mid) 100%);
    box-shadow: 0 6px 14px var(--shadow);
  }
  .card--front { left: 73px; }
  .card--back { left: 625px; }

  .company {
    position: absolute; left: 38px; top: 36px;
    font-family: "Cinzel", serif; font-weight: 600;
    font-size: 31px; letter-spacing: 0.5px; color: var(--ink-brown);
    white-space: nowrap;
  }
  .role {
    position: absolute; left: 38px; top: 86px;
    font-family: "Montserrat", sans-serif; font-weight: 500;
    font-size: 27px; color: var(--ink-brown);
  }
  .person {
    position: absolute; left: 38px; top: 146px;
    font-family: "Montserrat", sans-serif; font-weight: 400;
    font-size: 19px; color: var(--ink-brown);
  }
  .contacts { position: absolute; left: 38px; top: 220px; list-style: none; }
  .contacts li {
    display: flex; align-items: center; height: 35px;
    font-family: "Montserrat", sans-serif; font-size: 19px; color: var(--ink-brown);
  }
  .contacts svg { width: 24px; height: 24px; margin-right: 18px; flex: none; }

  .mini-brand {
    position: absolute; left: 384px; top: 232px; width: 90px;
    display: flex; flex-direction: column; align-items: center;
    color: var(--gold);
  }
  .mini-brand .mark-ring { width: 46px; height: 46px; border: 1.5px solid var(--gold); border-radius: 50%; }
  .mini-brand .brand-name {
    margin-top: 8px; font-family: "Cinzel", serif; font-weight: 600;
    font-size: 16px; letter-spacing: 0.5px;
  }
  .mini-brand .since { font-family: "Montserrat", sans-serif; font-size: 6px; letter-spacing: 1.5px; margin-top: 1px; }

  .brand {
    position: absolute; left: 0; right: 0; top: 70px;
    display: flex; flex-direction: column; align-items: center;
    color: var(--gold);
  }
  .brand .mark-ring { width: 144px; height: 144px; border: 3px solid var(--gold); border-radius: 50%; }
  .brand .brand-name {
    margin-top: 20px; font-family: "Cinzel", serif; font-weight: 600;
    font-size: 42px; letter-spacing: 6px;
  }
  .brand .since {
    margin-top: 2px; font-family: "Montserrat", sans-serif; font-weight: 500;
    font-size: 13px; letter-spacing: 3.5px; color: var(--ink-brown);
  }
</style>
</head>
<body>
<main class="canvas">
  <section class="card card--front">
    <h1 class="company">KORBALT SOLVANG</h1>
    <p class="role">CEO &amp; Founder</p>
    <p class="person">Lars Henrik Solvang</p>
    <ul class="contacts">
      <li>
        <svg viewBox="0 0 24 24" fill="none" stroke="var(--icon)" stroke-width="1.4"><rect x="7" y="2" width="10" height="20" rx="2"/><line x1="11" y1="18.5" x2="13" y2="18.5"/></svg>
        004791234567
      </li>
      <li>
        <svg viewBox="0 0 24 24" fill="none" stroke="var(--icon)" stroke-width="1.4"><rect x="2" y="5" width="20" height="14" rx="1"/><polyline points="2,5 12,13 22,5"/></svg>
        korbalt.llc@mailbox.com
      </li>
      <li>
        <svg viewBox="0 0 24 24" fill="none" stroke="var(--icon)" stroke-width="1.4"><circle cx="12" cy="12" r="10"/><ellipse cx="12" cy="12" rx="4.5" ry="10"/><line x1="2" y1="12" x2="22" y2="12"/><path d="M4 7h16M4 17h16"/></svg>
        www.korbalt.llc
      </li>
    </ul>
    <div class="mini-brand">
      <span class="mark-ring"></span>
      <span class="brand-name">KORBALT</span>
      <span class="since">SINCE 2025</span>
    </div>
  </section>

  <section class="card card--back">
    <div class="brand">
      <span class="mark-ring"></span>
      <span class="brand-name">KORBALT</span>
      <span class="since">SINCE 2026</span>
    </div>
  </section>
</main>
</body>
</html>
```